Korvex Global ltd. Stationaries
Full Stationary set
Korvex Global ltd. Stationaries  -
Creative Brief
Professional
Owen Pallister
VP, Sales MENA
Korvex Global Limited Zerhani Tower Office No. 614-616, 6th Floor Qasr Nadeem Road, Hessa P.O. Box 4827 Dubai, UAE
owen.pallister@korvexglb.example
korvexglb.example
All Size A4 (European Size) - Letterhead (Word Template, PDF, AI) - Purchase Order (Excel Template, PDF, AI) - Quotation (Excel Template, PDF, AI) - Invoice (Excel Template, PDF, AI) - Envelope (Big, Medium, Small) - Business Card (front and back) - Power Point Template - CD/DVD (label and jacket) - Folder
Broadcasting Solutions

```html
<!DOCTYPE html>
<html lang="en">
<head>
<meta charset="utf-8">
<title>Korvex Global ltd. Stationaries</title>
<link href="https://fonts.googleapis.com/css2?family=Open+Sans:wght@400;600;700&display=swap" rel="stylesheet">
<style>
  :root{
    --board:#a3a4a6;
    --paper:#ffffff;
    --brand-blue:#1f8fc4;
    --brand-blue-dark:#0c5f93;
    --brand-blue-light:#45b3e2;
    --ink:#3a3a3a;
    --ink-soft:#6a6a6a;
    --name-blue:#2a6fa8;
  }
  *{box-sizing:border-box;margin:0;padding:0}
  html,body{width:1200px;height:626px;overflow:hidden}
  body{background:var(--board);font-family:"Open Sans",Arial,sans-serif;color:var(--ink);position:relative}
  .item{position:absolute;background:var(--paper);box-shadow:0 1px 3px rgba(0,0,0,.25)}
  .brand{font-family:"Open Sans",Arial,sans-serif;font-weight:700;color:var(--ink);letter-spacing:.5px;display:flex;align-items:center;gap:6px;white-space:nowrap}
  .brand-dot{width:.8em;height:.8em;border-radius:50%;background:var(--brand-blue)}
  .band{position:absolute;background:linear-gradient(90deg,var(--brand-blue-dark),var(--brand-blue-light))}

  /* business card front */
  .card-front{left:34px;top:199px;width:144px;height:96px;border-radius:6px;
    background:linear-gradient(135deg,var(--brand-blue-light),var(--brand-blue-dark));
    display:flex;align-items:center;padding-left:18px}
  .card-front .brand{color:#fff;font-size:20px}
  .card-front .brand-dot{background:#fff}

  /* business card back */
  .card-back{left:34px;top:307px;width:144px;height:120px;border-radius:4px;text-align:center}
  .card-back .band{top:17px;height:5px}
  .card-back .band.l{left:0;width:34px}
  .card-back .band.r{right:0;width:34px}
  .card-back .brand{position:absolute;top:11px;left:50%;transform:translateX(-50%);font-size:13px}
  .card-back .person{position:absolute;top:46px;left:0;right:0}
  .person-name{font-size:7px;font-weight:700;color:var(--name-blue)}
  .person-role{font-size:4.5px;color:var(--ink-soft)}
  .card-back .contact{position:absolute;top:66px;left:6px;right:6px;font-size:3.6px;line-height:5.4px;color:var(--ink-soft)}
  .card-back .web{font-weight:700;color:var(--ink)}

  /* letterhead */
  .letterhead{left:233px;top:34px;width:367px;height:559px}
  .letterhead .band{top:31px;height:15px}
  .letterhead .band.l{left:0;width:115px}
  .letterhead .band.r{right:0;width:60px}
  .letterhead .brand{position:absolute;top:25px;left:50%;transform:translateX(-50%);font-size:22px}
  .letter-footer{position:absolute;bottom:14px;left:0;right:0;text-align:center;font-size:4.4px;line-height:6.4px;color:var(--ink-soft)}
  .letter-footer strong{color:var(--ink);font-weight:700}

  /* envelope back */
  .envelope-back{left:679px;top:79px;width:492px;height:168px}
  .envelope-back svg{position:absolute;inset:0}

  /* envelope front */
  .envelope-front{left:679px;top:336px;width:492px;height:197px}
  .envelope-front .band{top:32px;height:15px}
  .envelope-front .band.l{left:0;width:50px}
  .envelope-front .band.r{right:0;width:250px}
  .envelope-front .brand{position:absolute;top:26px;left:60px;font-size:22px}
  .envelope-address{position:absolute;right:18px;top:164px;width:360px;text-align:center;font-size:4.6px;line-height:6.6px;color:var(--ink-soft)}
  .envelope-address strong{color:var(--ink);font-weight:700}
</style>
</head>
<body>

  <section class="item card-front" aria-label="Business card front">
    <div class="brand"><span class="brand-dot"></span>KORVEX</div>
  </section>

  <section class="item card-back" aria-label="Business card back">
    <div class="band l"></div><div class="band r"></div>
    <div class="brand"><span class="brand-dot"></span>KORVEX</div>
    <div class="person">
      <p class="person-name">Owen Pallister</p>
      <p class="person-role">VP, Sales MENA</p>
    </div>
    <div class="contact">
      <p>Korvex Global Limited, Zerhani Tower, Office No. 614-616, 6th Floor</p>
      <p>Qasr Nadeem Road, Hessa, P.O. Box 4827, Dubai, UAE</p>
      <p>Phone: +971 4 555 0182 | Fax: +971 4 555 0183</p>
      <p>owen.pallister@korvexglb.example</p>
      <p class="web">korvexglb.example</p>
    </div>
  </section>

  <section class="item letterhead" aria-label="Letterhead">
    <div class="band l"></div><div class="band r"></div>
    <div class="brand"><span class="brand-dot"></span>KORVEX</div>
    <div class="letter-footer">
      <p><strong>Korvex Global Limited</strong></p>
      <p>Zerhani Tower, Office No. 614-616, 6th Floor, Qasr Nadeem Road, Hessa, P.O. Box 4827, Dubai, UAE</p>
      <p>Phone: +971 4 555 0182 | Email: info@korvexglb.example | korvexglb.example</p>
    </div>
  </section>

  <section class="item envelope-back" aria-label="Envelope back">
    <svg width="492" height="168" viewBox="0 0 492 168" aria-hidden="true">
      <defs>
        <linearGradient id="flapFill" x1="0" y1="0" x2="0" y2="1">
          <stop offset="0" stop-color="#0c5f93"/>
          <stop offset="1" stop-color="#45b3e2"/>
        </linearGradient>
      </defs>
      <path d="M0 0 H492 V48 C430 52 300 58 262 78 Q246 86 230 78 C192 58 62 52 0 48 Z" fill="url(#flapFill)"/>
    </svg>
  </section>

  <section class="item envelope-front" aria-label="Envelope front">
    <div class="band l"></div><div class="band r"></div>
    <div class="brand"><span class="brand-dot"></span>KORVEX</div>
    <div class="envelope-address">
      <p><strong>Korvex Global Limited</strong></p>
      <p>Zerhani Tower, Office No. 614-616, 6th Floor, Qasr Nadeem Road, Hessa, P.O. Box 4827, Dubai, UAE</p>
      <p>Phone: +971 4 555 0182 | Email: info@korvexglb.example | korvexglb.example</p>
    </div>
  </section>

</body>
</html>
```